Redesigned PowerPoint template for Restaurant Services Company

We need a redesigned company template for powerpoints. looking for something modern and easy to use. If we like it, we will add additional products for the design (letterhead, social media banners, etc).

Target Market(s)

restaurant owners, and franchise owners

Font styles to use
Serif
Sans Serif

Colors
0355a3
f0474d
ffffff

Requirements
Must have
• - something that uses our colors in a modern way
- easy to use
- something that is eye catching
Nice to have
• - multiple slide types (picture and text, graphic and text, bulleted text, etc)
- easy way to swap out our prospects logo and have our prospects logo displayed throughout the deck
Should not have
• should not have locked or anchored fields making it difficult to edit

```html
<!DOCTYPE html>
<html lang="en">
<head>
<meta charset="utf-8">
<title>LVP Overview 2021 – Slide Deck</title>
<link href="https://fonts.googleapis.com/css2?family=Fira+Sans:ital,wght@0,300;0,400;0,500;0,600;0,700;1,300;1,400;1,600&display=swap" rel="stylesheet">
<style>
:root{
  --red:#f0474d;
  --blue:#0355a3;
  --white:#ffffff;
  --ink:#1d1d1f;
  --grey:#3a3a3a;
  --black:#000000;
}
*{box-sizing:border-box;margin:0;padding:0}
html,body{width:1200px;height:1158px;overflow:hidden;background:var(--black)}
body{font-family:"Fira Sans",Arial,sans-serif;color:var(--ink)}
.board{position:absolute;left:0;top:0;width:1960px;height:1891px;transform:scale(.612245);transform-origin:0 0}
.slide{position:absolute;width:622px;height:349px;background:var(--white);overflow:hidden}
.slide > *{position:absolute}
.band{background:var(--red);left:0;top:0;width:622px}
.edge{right:0;top:0;width:4px;height:349px;background:var(--red)}
.foot-url{left:250px;top:328px;font-size:8.5px;color:var(--red)}
.page{right:18px;top:328px;font-size:8.5px;color:var(--red)}
.on-red .foot-url,.on-red .page{color:var(--white)}
.logo{display:flex;align-items:center;gap:5px;font-weight:700;font-size:9px;line-height:1.05;color:var(--blue);letter-spacing:.5px;width:90px}
.logo i{display:block;width:10px;height:10px;background:var(--red);flex:none}
.logo.light{color:var(--white)}
.logo.light i{background:var(--white)}
.rule{width:3px;background:var(--red)}
.rule.white{background:var(--white)}
.kicker{font-weight:600;font-size:20px;line-height:1.3}
.kicker .r{color:var(--red)}
.kicker .b{color:var(--blue)}
.slide-title{font-weight:600;color:var(--white);font-size:29px;line-height:1.15}
.lead{color:var(--white);font-weight:300;font-size:16px;line-height:1.32}
.bullets{list-style:none}
.bullets li{position:relative;padding-left:18px}
.bullets li::before{content:"";position:absolute;left:0;top:.45em;width:5px;height:5px;background:var(--red)}
.glance li{font-size:10.5px;font-weight:600;line-height:1.3;margin-bottom:6px}
.col-head{color:var(--red);font-weight:600;font-size:12px;line-height:1.3}
.col-list li{font-size:9px;line-height:1.28;margin-bottom:9px;color:var(--grey)}
.item-head{color:var(--red);font-weight:600;font-size:12.5px}
.item-text{font-size:9px;line-height:1.35;color:var(--grey)}
.icon{fill:none;stroke:var(--red);stroke-width:1.4}
.tab{top:95px;width:123px;height:80px;text-align:center;padding-top:14px}
.tab b{display:block;font-size:22px;font-weight:600}
.tab span{display:block;font-size:12.5px;font-weight:600;margin-top:6px}
.tab.light{background:var(--white);color:var(--blue)}
.tab.dark{background:var(--red);color:var(--white)}
.tab-note{top:205px;width:110px;text-align:center;font-size:9px;line-height:1.3;color:var(--grey)}
.node{border-radius:50%;color:var(--white);display:flex;align-items:center;justify-content:center;text-align:center;font-weight:600;font-size:10px;line-height:1.25}
.node.red{background:var(--red)}
.node.blue{background:var(--blue)}
.node-box{border:1.5px solid var(--red);border-radius:12px}
.node-box.blue{border-color:var(--blue)}
.node-text{font-size:9px;line-height:1.3;color:var(--grey)}
.svc-head{color:var(--red);font-weight:500;font-size:14.5px}
.svc-list li{font-size:8.6px;font-weight:600;line-height:1.35}
.svc-list li::before{width:4px;height:4px}
.cog{fill:none;stroke:var(--blue);stroke-width:1.3}
.quote-list li{font-size:8.8px;line-height:1.35;margin-bottom:12px}
.quote-list em{font-weight:600}
.step{top:160px;width:120px;text-align:center;color:var(--white);font-weight:300;font-size:13.5px;line-height:1.25}
.contact{color:var(--white);font-size:9.5px;line-height:1.25}
.contact b{font-weight:600}
.photo{background:linear-gradient(135deg,#8fb7b9 0%,#b8a48a 45%,#6d4a3a 75%,#3d2e2a 100%)}
.map{background:linear-gradient(160deg,#2f6cb3,#0355a3)}
</style>
</head>
<body>
<div class="board">

  <!-- 01 Cover -->
  <section class="slide" style="left:21px;top:23px">
    <div class="band" style="height:65px"></div>
    <div style="left:36px;top:84px;width:172px;height:172px;border:1.5px solid var(--red);border-radius:50%"></div>
    <div class="logo" style="left:75px;top:158px;font-size:12px;width:110px"><i></i>LIBERTY VENUE PARTNERS</div>
    <h1 style="left:238px;top:80px;color:var(--red);font-size:47px;font-weight:700">LVP Overview</h1>
    <div style="left:238px;top:140px;color:var(--red);font-size:32px;font-weight:600">2021</div>
    <div style="left:240px;top:190px;width:3px;height:66px;background:var(--blue)"></div>
    <div style="left:262px;top:188px;color:var(--blue);font-size:20px;font-weight:300">Prepared for</div>
    <div style="left:262px;top:218px;color:var(--blue);font-size:28px;font-weight:600">Maison Sucrée</div>
    <div class="foot-url">www.libertyvenuepartners.com</div>
    <div class="page">01</div>
  </section>

  <!-- 02 At a glance -->
  <section class="slide" style="left:669px;top:23px">
    <div class="rule" style="left:40px;top:38px;height:46px"></div>
    <div class="kicker" style="left:64px;top:34px"><span class="r">LVP</span><br><span class="b">At-A-Glance</span></div>
    <ul class="bullets glance" style="left:40px;top:108px;width:400px">
      <li>Founded and Based in Austin, TX in 2017</li>
      <li>Veteran Owned and Operated</li>
      <li>Technology, Construction, and Managed Operations Services Company Focused On the Restaurant Industry</li>
      <li>Experienced Teams of Restaurant Operators</li>
      <li>Nearshore Technology Solution Center Offering 24/7 Support</li>
      <li>Successfully Delivered Over 200 Projects Nationally (TX, OH, MI, OK, KS) Since 2017</li>
      <li>Portion Of All Profits To Benefit Veteran Charities</li>
    </ul>
    <div class="map" role="img" aria-label="Map of the Americas marking the Austin, Texas office" style="left:430px;top:28px;width:188px;height:275px;border-radius:40px 20px 60px 30px"></div>
    <div style="left:465px;top:70px;width:108px;height:28px;background:var(--red);color:var(--white);font-size:8px;text-align:center;line-height:28px">Austin, TX</div>
    <div style="left:456px;top:100px;width:50px;height:16px;background:var(--red);color:var(--white);font-size:7.5px;text-align:center;line-height:16px">our office</div>
    <div class="edge"></div>
    <div class="logo" style="left:16px;top:302px"><i></i>LIBERTY VENUE PARTNERS</div>
    <div class="foot-url">www.libertyvenuepartners.com</div>
    <div class="page">02</div>
  </section>

  <!-- 03 Mission -->
  <section class="slide on-red" style="left:1317px;top:23px">
    <div class="band" style="width:525px;height:349px"></div>
    <h2 class="slide-title" style="left:40px;top:30px;font-size:28px">What we stand for?</h2>
    <div style="left:44px;top:68px;color:var(--white);font-size:48px;font-weight:700">“</div>
    <p style="left:88px;top:94px;width:390px;color:var(--white);font-style:italic;font-weight:300;font-size:15px;line-height:1.38">Our desire to improve the quality and standards of our industry, for our clients, while making a difference in people’s lives, is our mission statement. This is LVP!”</p>
    <div style="left:88px;top:186px;color:var(--white);font-size:14px;font-weight:300">– <b style="font-weight:600">Daniel Marlowe</b>, LVP CEO</div>
    <div class="logo light" style="left:20px;top:302px"><i></i>LIBERTY VENUE PARTNERS</div>
    <div class="foot-url">www.libertyvenuepartners.com</div>
    <div class="page" style="color:var(--red)">03</div>
  </section>

  <!-- 04 What we do -->
  <section class="slide" style="left:21px;top:396px">
    <div class="band" style="height:255px"></div>
    <h2 class="slide-title" style="left:47px;top:34px;font-size:28px">What we do</h2>
    <div class="rule white" style="left:48px;top:92px;height:94px"></div>
    <p class="lead" style="left:83px;top:105px;width:480px">Leveraging an end-to-end integrated services portfolio offering, ranging from technology, construction, and restaurant managed operation services, LVP delivers results that move the needle!</p>
    <div class="logo" style="left:16px;top:302px"><i></i>LIBERTY VENUE PARTNERS</div>
    <div class="foot-url">www.libertyvenuepartners.com</div>
    <div class="page">04</div>
  </section>

  <!-- 05 Moving the needle -->
  <section class="slide" style="left:669px;top:396px">
    <div class="rule" style="left:40px;top:35px;height:28px"></div>
    <div style="left:64px;top:33px;font-size:22px;font-weight:600;color:var(--blue)">Moving the Needle with <span style="color:var(--red)">LVP360</span></div>
    <div style="left:97px;top:88px;width:36px;height:10px;border-radius:50%;background:var(--blue)"></div>
    <div style="left:289px;top:88px;width:36px;height:10px;border-radius:50%;background:var(--blue)"></div>
    <div style="left:480px;top:88px;width:36px;height:10px;border-radius:50%;background:var(--blue)"></div>
    <div class="col-head" style="left:45px;top:114px">Operational Efficiency</div>
    <ul class="bullets col-list" style="left:45px;top:155px;width:140px">
      <li>Evaluate existing business processes for best practice adoption, automation, and shared services enablement</li>
      <li>Assess technology landscape, integration, and support</li>
    </ul>
    <div class="col-head" style="left:246px;top:114px">New and Increased<br>Revenue Streams</div>
    <ul class="bullets col-list" style="left:238px;top:171px;width:145px">
      <li>Brand refresh for capture of new demographics</li>
      <li>Remodel and train existing network</li>
      <li>New territory construction expansion</li>
    </ul>
    <div class="col-head" style="left:440px;top:114px">Increasing Company<br>Value</div>
    <ul class="bullets col-list" style="left:432px;top:171px;width:150px">
      <li>Identify and remediate under performing locations</li>
      <li>Implement managed operations for company store or franchise location</li>
      <li>Increase system-wide AUV, and increase company’s market cap</li>
    </ul>
    <div class="logo" style="left:16px;top:302px"><i></i>LIBERTY VENUE PARTNERS</div>
    <div class="foot-url">www.libertyvenuepartners.com</div>
    <div class="page">05</div>
  </section>

  <!-- 06 How we do it -->
  <section class="slide" style="left:1317px;top:396px">
    <div class="band" style="height:255px"></div>
    <h2 class="slide-title" style="left:47px;top:34px;font-size:28px">How we do it</h2>
    <div class="rule white" style="left:48px;top:92px;height:94px"></div>
    <p class="lead" style="left:83px;top:105px;width:500px">LVP360 is an end-to-end integrated services offering that takes a wholistic view of your company to improve operational efficiencies, identify new revenue streams, and increase overall profitability.</p>
    <div class="logo" style="left:16px;top:302px"><i></i>LIBERTY VENUE PARTNERS</div>
    <div class="foot-url">www.libertyvenuepartners.com</div>
    <div class="page">06</div>
  </section>

  <!-- 07 Value ID -->
  <section class="slide" style="left:21px;top:770px">
    <div class="rule" style="left:40px;top:40px;height:48px"></div>
    <div class="kicker" style="left:64px;top:36px"><span class="r">LVP</span><br><span class="b">Value ID</span></div>
    <svg style="left:296px;top:40px" width="34" height="260" viewBox="0 0 34 260">
      <g class="icon">
        <circle cx="17" cy="9" r="6"/><path d="M6 25c0-7 5-10 11-10s11 3 11 10z"/>
        <path d="M5 68l8-4 8 4 8-4v20l-8 4-8-4-8 4z M13 64v20 M21 68v20"/>
        <rect x="5" y="117" width="24" height="15"/><path d="M9 128l5-5 4 3 6-6 M17 132v6"/>
        <path d="M5 194h24 M7 194v-12h4v12 M13 194v-18h4v18 M19 194v-9h4v9 M25 194v-6h3v6"/>
        <circle cx="17" cy="234" r="12"/><path d="M17 234v-12 M17 234l10 6"/>
      </g>
      <g stroke="var(--blue)" stroke-width="2.5"><path d="M17 35v14 M17 95v14 M17 148v14 M17 205v14"/></g>
    </svg>
    <div class="item-head" style="left:346px;top:38px">Customer ID</div>
    <div class="item-text" style="left:346px;top:58px;width:190px">Lorem ipsum dolor sit amet, consectetur adipiscing elit.</div>
    <div class="item-head" style="right:345px;top:90px;text-align:right">Geographies</div>
    <div class="item-text" style="right:345px;top:110px;width:190px;text-align:right">Lorem ipsum dolor sit amet, consectetur adipiscing elit.</div>
    <div class="item-head" style="left:346px;top:145px">Operational Effeciency</div>
    <div class="item-text" style="left:346px;top:165px;width:190px">Lorem ipsum dolor sit amet, consectetur adipiscing elit.</div>
    <div class="item-head" style="right:345px;top:196px;text-align:right">Peer Benchmarking</div>
    <div class="item-text" style="right:345px;top:216px;width:190px;text-align:right">Lorem ipsum dolor sit amet, consectetur adipiscing elit.</div>
    <div class="item-head" style="left:346px;top:254px">SWOT Analysis</div>
    <div class="item-text" style="left:346px;top:274px;width:190px">Lorem ipsum dolor sit amet, consectetur adipiscing elit.</div>
    <div class="edge"></div>
    <div class="logo" style="left:16px;top:302px"><i></i>LIBERTY VENUE PARTNERS</div>
    <div class="foot-url">www.libertyvenuepartners.com</div>
    <div class="page">07</div>
  </section>

  <!-- 08 ValueMap -->
  <section class="slide" style="left:669px;top:770px">
    <div class="band" style="height:145px"></div>
    <h2 style="left:0;top:18px;width:622px;text-align:center;color:var(--white);font-size:40px;font-weight:600">LVP ValueMap</h2>
    <div class="tab light" style="left:63px"><b>01</b><span>Alignment</span></div>
    <div class="tab dark" style="left:186px"><b>02</b><span>Prioritize</span></div>
    <div class="tab light" style="left:309px"><b>03</b><span>Design</span></div>
    <div class="tab dark" style="left:432px"><b>04</b><span>Communicate</span></div>
    <div class="tab-note" style="left:69px">Lorem ipsum dolor sit amet, consectetur adipiscing elit,</div>
    <div class="tab-note" style="left:192px">Lorem ipsum dolor sit amet, consectetur adipiscing elit,</div>
    <div class="tab-note" style="left:315px">Lorem ipsum dolor sit amet, consectetur adipiscing elit,</div>
    <div class="tab-note" style="left:438px">Lorem ipsum dolor sit amet, consectetur adipiscing elit,</div>
    <div class="logo" style="left:16px;top:302px"><i></i>LIBERTY VENUE PARTNERS</div>
    <div class="foot-url">www.libertyvenuepartners.com</div>
    <div class="page">08</div>
  </section>

  <!-- 09 Execution network -->
  <section class="slide" style="left:1317px;top:770px">
    <div class="rule" style="left:40px;top:38px;height:22px"></div>
    <div style="left:64px;top:36px;font-size:20px;font-weight:600;color:var(--blue);word-spacing:4px"><span style="color:var(--red)">LVP</span> Execution Network</div>
    <div class="logo" style="left:520px;top:26px"><i></i>LIBERTY VENUE PARTNERS</div>
    <div class="node-box" style="left:75px;top:112px;width:157px;height:82px"></div>
    <div class="node red" style="left:43px;top:88px;width:64px;height:64px">Expert<br>Resoues</div>
    <div class="node-text" style="left:118px;top:128px;width:100px">Lorem ipsum dolor sit amet, consectetur adipiscing elit, sed do eiusmo</div>
    <div class="node-box blue" style="left:287px;top:112px;width:157px;height:82px"></div>
    <div class="node blue" style="left:255px;top:88px;width:64px;height:64px">LVP<br>PMO</div>
    <div class="node-text" style="left:330px;top:128px;width:100px">Lorem ipsum dolor sit amet, consectetur adipiscing elit, sed do eiusmo</div>
    <div class="node-box" style="left:500px;top:112px;width:98px;height:200px"></div>
    <div class="node red" style="left:465px;top:88px;width:70px;height:70px;font-size:9px">Nearshore<br>Technology<br>Center</div>
    <div class="node-text" style="left:505px;top:160px;width:90px;text-align:center">Lorem ipsum dolor sit amet, consectetur adipiscing elit, sed do eiusmod tempor incididunt ut labore et dolore magna aliqua</div>
    <div class="node-box blue" style="left:75px;top:230px;width:157px;height:82px"></div>
    <div class="node blue" style="left:43px;top:206px;width:64px;height:64px">Product<br>Sourcing</div>
    <div class="node-text" style="left:118px;top:246px;width:100px">Lorem ipsum dolor sit amet, consectetur adipiscing elit, sed do eiusmo</div>
    <div class="node-box" style="left:287px;top:230px;width:157px;height:82px"></div>
    <div class="node red" style="left:255px;top:206px;width:64px;height:64px;font-size:8.5px">Restaurant<br>Operations<br>Team</div>
    <div class="node-text" style="left:330px;top:244px;width:100px">Lorem ipsum dolor sit amet, consectetur adipiscing elit, sed do eiusmo</div>
    <div class="foot-url">www.libertyvenuepartners.com</div>
    <div class="page">09</div>
  </section>

  <!-- 10 Detailed offerings -->
  <section class="slide on-red" style="left:21px;top:1143px">
    <div class="band" style="width:310px;height:349px"></div>
    <div class="photo" role="img" aria-label="Photo of a takeaway coffee cup beside a box of macarons on a wooden table" style="left:310px;top:0;width:312px;height:349px"></div>
    <h2 class="slide-title" style="left:38px;top:26px;font-size:26px">Detailed Service<br>Offerings</h2>
    <p style="left:38px;top:122px;width:220px;color:var(--white);font-weight:600;font-size:13.5px;line-height:1.38">“LVP’s portfolio of service offerings, created for the restaurant industry, provides unmatched value and clarity to your business!”</p>
    <div style="right:342px;top:250px;color:var(--white);font-size:11px">– <b style="font-weight:600">Owen Hartley</b>, LVP COO</div>
    <div class="logo light" style="left:20px;top:302px"><i></i>LIBERTY VENUE PARTNERS</div>
    <div class="foot-url">www.libertyvenuepartners.com</div>
    <div class="page">10</div>
  </section>

  <!-- 11 Technology services -->
  <section class="slide" style="left:669px;top:1143px">
    <div class="band" style="height:65px"></div>
    <h2 class="slide-title" style="left:70px;top:14px;font-size:30px">Technology Services</h2>
    <svg style="left:60px;top:83px" width="28" height="200" viewBox="0 0 28 200">
      <g class="cog"><circle cx="13" cy="12" r="9" stroke-dasharray="3 2.2" stroke-width="4"/><circle cx="13" cy="12" r="4"/>
      <circle cx="13" cy="98" r="9" stroke-dasharray="3 2.2" stroke-width="4"/><circle cx="13" cy="98" r="4"/>
      <circle cx="13" cy="172" r="9" stroke-dasharray="3 2.2" stroke-width="4"/><circle cx="13" cy="172" r="4"/></g>
    </svg>
    <div class="svc-head" style="left:98px;top:84px">Software Implementations</div>
    <ul class="bullets svc-list" style="left:143px;top:104px;width:300px">
      <li>Back-office software selection and implementation services (ERP, CRM, POS, payroll, accounting, etc)</li>
      <li>Hardware and software upgrades</li>
      <li>Cloud strategies and deployments</li>
    </ul>
    <div class="svc-head" style="left:98px;top:170px">Application Development</div>
    <ul class="bullets svc-list" style="left:143px;top:190px;width:300px">
      <li>Mobile application development</li>
      <li>Business analytics dashboard development</li>
      <li>Disparate systems integration (3<sup style="font-size:6px">rd</sup> party delivery, etc)</li>
    </ul>
    <div class="svc-head" style="left:98px;top:244px">Application Management Support</div>
    <ul class="bullets svc-list" style="left:143px;top:264px;width:420px">
      <li>Complete 24/7 IT remote support from LVP’s nearshore Technology Solution Centers</li>
      <li>IT Managed services for hardware, software, and databases</li>
      <li>Restaurant experienced technologists</li>
    </ul>
    <div class="logo" style="left:16px;top:302px"><i></i>LIBERTY VENUE PARTNERS</div>
    <div class="foot-url">www.libertyvenuepartners.com</div>
    <div class="page">11</div>
  </section>

  <!-- 12 Construction services -->
  <section class="slide" style="left:1317px;top:1143px">
    <div class="band" style="height:65px"></div>
    <h2 class="slide-title" style="left:60px;top:14px;font-size:30px">Construction Services</h2>
    <svg style="left:445px;top:2px" width="120" height="62" viewBox="0 0 120 62">
      <g fill="none" stroke="var(--white)" stroke-width="1.5">
        <circle cx="62" cy="30" r="16"/><circle cx="12" cy="30" r="6"/><circle cx="108" cy="8" r="5"/><circle cx="100" cy="52" r="5"/><circle cx="70" cy="4" r="3"/>
        <path d="M18 30h28 M76 23l27-13 M75 39l21 10 M64 14l5-8"/>
      </g>
    </svg>
    <svg style="left:60px;top:83px" width="28" height="200" viewBox="0 0 28 200">
      <g class="cog"><circle cx="13" cy="12" r="9" stroke-dasharray="3 2.2" stroke-width="4"/><circle cx="13" cy="12" r="4"/>
      <circle cx="13" cy="98" r="9" stroke-dasharray="3 2.2" stroke-width="4"/><circle cx="13" cy="98" r="4"/>
      <circle cx="13" cy="184" r="9" stroke-dasharray="3 2.2" stroke-width="4"/><circle cx="13" cy="184" r="4"/></g>
    </svg>
    <div class="svc-head" style="left:98px;top:84px">New Restaurant Consulting</div>
    <ul class="bullets svc-list" style="left:143px;top:104px;width:470px">
      <li>Concept Development</li>
      <li>Site Development Consulting</li>
      <li>Startup Consulting</li>
      <li>Corporate Contract Staffing (Marketing, FBC’s, Operations, and Training)</li>
    </ul>
    <div class="svc-head" style="left:98px;top:170px">Existing Restaurant Consulting</div>
    <ul class="bullets svc-list" style="left:143px;top:190px;width:470px">
      <li>Operational Analysis</li>
      <li>Quality Assurance and Audit Services</li>
      <li>GM Operations Training</li>
      <li>Corporate Contract Staffing (Marketing, FBC’s, Operations, and Training)</li>
    </ul>
    <div class="svc-head" style="left:98px;top:256px">Outsourced Restaurant Management</div>
    <ul class="bullets svc-list" style="left:143px;top:276px;width:470px">
      <li>Operational Takeover of Existing Underperforming Restaurant Locations</li>
      <li>Corporate Owned or Franchisee Models</li>
      <li>Multiple Deal Structures Available (Royalties, Profit Sharing, Rent+, etc)</li>
    </ul>
    <div class="logo" style="left:16px;top:302px"><i></i>LIBERTY VENUE PARTNERS</div>
    <div class="foot-url">www.libertyvenuepartners.com</div>
    <div class="page">12</div>
  </section>

  <!-- 13 Testimonials -->
  <section class="slide" style="left:21px;top:1516px">
    <div class="band" style="height:65px"></div>
    <h2 class="slide-title" style="left:60px;top:14px;font-size:29px">Don’t take our word from it</h2>
    <svg style="left:470px;top:-6px" width="95" height="62" viewBox="0 0 95 62">
      <path d="M47 4c24 0 44 9 44 22s-20 22-44 22c-6 0-12-1-17-2l-16 11 4-14C8 39 3 33 3 26 3 13 23 4 47 4z" fill="none" stroke="var(--white)" stroke-width="1.5"/>
    </svg>
    <ul class="bullets quote-list" style="left:40px;top:95px;width:540px">
      <li><em>“By utilizing LVP’s different services offerings, Brisket Barn identified numerous aspects of our business that significantly impacted profitability”</em> - Laura Penn, President of Brisket Barn Restaurants</li>
      <li><em>“LVP assessed our environment, developed a strategic roadmap, and implemented solutions that changed our forecasted profitability. We then utilized LVP’s support services to protect those gains!”</em> - Carl Mercer, CIO Ridge Farms</li>
      <li><em>“Fantastic work Owen, Daniel, Sam and the whole team at Liberty Venue Partners. Professionalism, honesty and class throughout. Can’t wait to work with LVP on my 9 other locations!”</em> - TJ Holloway, Brisket Barn’s Franchisee</li>
      <li><em>“LVP handled everything with my store conversion! They far exceeded our expectations, and the results are amazing!”</em><br>- Nina Carver, Restaurant Owner</li>
      <li><em>“I chose LVP because it was obvious my best interests came first and foremost. They make every effort to minimize store disruption”</em> – Ruth Delacroix, Restaurant Owner</li>
    </ul>
    <div class="logo" style="left:16px;top:302px"><i></i>LIBERTY VENUE PARTNERS</div>
    <div class="foot-url">www.libertyvenuepartners.com</div>
    <div class="page">13</div>
  </section>

  <!-- 14 Next steps -->
  <section class="slide" style="left:669px;top:1516px">
    <div class="band" style="height:255px"></div>
    <h2 style="left:0;top:30px;width:622px;text-align:center;color:var(--white);font-size:44px;font-weight:600">Next Steps</h2>
    <div style="left:0;top:136px;width:622px;height:2px;background:var(--white)"></div>
    <svg style="left:0;top:126px" width="622" height="22" viewBox="0 0 622 22">
      <g fill="var(--blue)" stroke="var(--white)" stroke-width="2.5">
        <circle cx="85" cy="11" r="7"/><circle cx="236" cy="11" r="7"/><circle cx="387" cy="11" r="7"/><circle cx="531" cy="11" r="7"/>
      </g>
    </svg>
    <div class="step" style="left:25px">Determine which LVP services need to be utilized</div>
    <div class="step" style="left:176px">Confirm scope and locations for 2020/2021 remodels</div>
    <div class="step" style="left:327px">Develop pricing and contract agreements</div>
    <div class="step" style="left:471px">Develop prioritized rollout plan</div>
    <div class="logo" style="left:16px;top:302px"><i></i>LIBERTY VENUE PARTNERS</div>
    <div class="foot-url">www.libertyvenuepartners.com</div>
    <div class="page">14</div>
  </section>

  <!-- 15 Contact -->
  <section class="slide on-red" style="left:1317px;top:1516px">
    <div class="band" style="width:310px;height:349px"></div>
    <h2 class="slide-title" style="left:112px;top:30px;font-size:26px">Contact Us</h2>
    <div class="contact" style="left:50px;top:92px"><b>Toll-free:</b> 800-555-0142</div>
    <div class="contact" style="left:50px;top:126px"><b>Website:</b> www.libertyvenuepartners.com</div>
    <div class="contact" style="left:50px;top:160px"><b>Email:</b> daniel@libertyvenuepartners.com<br><span style="padding-left:30px">owen@libertyvenuepartners.com</span></div>
    <div class="contact" style="left:50px;top:212px"><b>Facebook:</b> @LibertyVenuePartners</div>
    <div class="contact" style="left:50px;top:242px;line-height:1.8"><b>4820 Cedar Bend Dr,</b> #210<br><b>Austin, TX</b> 78745</div>
    <div role="img" aria-label="Phone screen placeholder for a product screenshot" style="left:402px;top:42px;width:129px;height:268px;background:#000;border-radius:20px">
      <div style="position:absolute;left:62px;top:12px;width:4px;height:2px;background:#fff"></div>
      <div style="position:absolute;left:10px;top:38px;width:109px;height:192px;background:var(--blue);color:var(--white);font-size:7px;text-align:center;padding-top:86px;line-height:1.3">Place your screenshot<br>HERE</div>
    </div>
    <div class="logo light" style="left:20px;top:302px"><i></i>LIBERTY VENUE PARTNERS</div>
    <div class="foot-url">www.libertyvenuepartners.com</div>
    <div class="page" style="color:var(--red)">15</div>
  </section>

</div>
</body>
</html>
```